Fernhollow Glow Clinic is a rebranding of fernhollowfootcare.com.au. The business provides Medical Injectables (botox and fillers) Laser and IPL therapies, Podiatry and remedial massage. We have a logo already done (yay! sketch hive!) you can download it here: http://fernhollowglowclinic.com/brand_assets.zip . We are after a clean, long scrolling website (in the style of quvaret.com). There will be 6 subpages (or sections depending on how you create it) (1) Cosmetic Injections (2) Podiatry (3) Remedial Massage (4) Laser Therapies (5) Skin Care (6) Customer Club and Special Offers. The target demographic is wealthy or aspirational women 35+.

Font styles to use
Sans Serif

Colors
9bcb3c
33a6d7

Requirements
Must have
• Simple, clean long scroller like quvaret.com
Nice to have
• Congruence with existing corporate identity.

```html
<!DOCTYPE html>
<html lang="en">
<head>
<meta charset="utf-8">
<title>Fernhollow Glow Clinic</title>
<link href="https://fonts.googleapis.com/css2?family=Open+Sans:wght@300;400;600;700&family=Cinzel:wght@400;700&display=swap" rel="stylesheet">
<style>
:root{
  --green:#9bcb3c;
  --green-dark:#7fae25;
  --blue:#33a6d7;
  --navy:#1f3550;
  --ink:#444;
  --muted:#8a8a8a;
  --cream:#f4f3ee;
  --line:#e2e2e2;
  --grey-btn:#6d6d6d;
  --white:#fff;
}
*{box-sizing:border-box;margin:0;padding:0}
html,body{width:1200px;height:2328px;overflow:hidden;background:var(--white);font-family:"Open Sans",Arial,sans-serif;color:var(--ink)}
.page{position:relative;width:1200px;height:2328px}
.topbar{height:24px;display:flex;justify-content:space-between;align-items:center;padding:0 22px;font-size:12px;color:#555;border-bottom:1px solid var(--line)}
.topbar .links span{margin:0 8px}
.topbar .links span:first-child{margin-left:0}
.topbar .follow{display:flex;align-items:center;gap:6px}
.topbar .dot{width:13px;height:13px;border-radius:50%;background:#9a9a9a}
.header{height:108px;display:flex;justify-content:space-between;align-items:flex-start;padding:0 40px 0 30px}
.brand{display:flex;align-items:center;gap:12px;margin-top:34px}
.brand .mark{width:26px;height:26px;border-radius:50%;background:var(--green)}
.brand .name{font-size:24px;font-weight:600;color:var(--green-dark);letter-spacing:.5px}
.nav{display:flex;align-items:stretch;height:108px}
.nav a{display:flex;align-items:center;padding:0 16px;font-size:14px;color:#555;text-decoration:none;border-left:1px solid var(--line)}
.nav a.active{border-top:4px solid var(--green);box-shadow:0 0 6px rgba(0,0,0,.15);background:var(--white)}
.nav .search{display:flex;align-items:center;padding:0 16px;border-left:1px solid var(--line)}
.hero{position:relative;height:458px;background:
  radial-gradient(ellipse 260px 200px at 150px 120px,rgba(245,245,248,.9),transparent 70%),
  radial-gradient(ellipse 420px 120px at 420px 300px,rgba(214,160,120,.85),transparent 70%),
  radial-gradient(ellipse 180px 140px at 560px 360px,rgba(232,225,220,.9),transparent 70%),
  radial-gradient(ellipse 260px 260px at 1080px 140px,rgba(150,160,170,.7),transparent 70%),
  radial-gradient(ellipse 200px 120px at 290px 200px,rgba(120,190,220,.55),transparent 70%),
  linear-gradient(100deg,#9a8f8a 0%,#d8ccc4 30%,#ece9e5 60%,#c9cfd4 100%)}
.hero .tagline{position:absolute;left:700px;top:162px;font-family:"Cinzel",Georgia,serif}
.hero .tagline .small{font-size:20px;letter-spacing:1px;color:var(--green)}
.hero .tagline .big{font-size:30px;font-weight:700;color:#6fae2a;margin-top:2px}
.hero .arrow{position:absolute;top:220px;width:30px;height:34px;background:rgba(60,60,60,.6);display:flex;align-items:center;justify-content:center}
.hero .arrow.left{left:0}.hero .arrow.right{right:0}
.rule{height:6px;background:var(--green)}
.services{height:480px;background:var(--cream);padding-top:92px;display:flex;justify-content:center;gap:36px}
.service{width:180px;text-align:center}
.service .photo{width:164px;height:164px;border-radius:50%;margin:0 auto;border:5px solid var(--white);box-shadow:0 0 0 1px #ddd}
.service h3{margin-top:14px;font-size:14px;font-weight:600;color:var(--blue)}
.service p{font-size:11px;color:#666;line-height:15px;margin-top:4px;padding:0 8px}
.btn-more{display:inline-block;margin-top:12px;width:58px;height:22px;line-height:22px;font-size:11px;color:var(--white);background:var(--grey-btn)}
.btn-more.primary{background:var(--blue)}
.newsletter{position:relative;height:125px;background:linear-gradient(90deg,#1c3149,#2c4863 55%,#b9a294 80%,#39506a);display:flex;align-items:center;padding-left:140px;gap:18px}
.newsletter .label{color:var(--white);font-size:13px;line-height:17px;width:170px}
.newsletter .field{width:240px;height:28px;background:var(--white);font-size:11px;color:#999;padding:6px 10px}
.newsletter .field.wide{width:270px;margin-left:6px}
.newsletter .submit{height:28px;padding:0 16px;background:var(--navy);color:var(--white);font-size:12px;font-weight:700;display:flex;align-items:center;border:1px solid #5d7894}
.gallery{height:590px;background:var(--cream);text-align:center;padding-top:64px}
.gallery h2{font-size:20px;font-weight:700;color:#555;letter-spacing:1px}
.gallery .bar{width:60px;height:3px;background:var(--green);margin:10px auto 12px}
.gallery .sub{font-size:12px;color:var(--muted);font-style:italic}
.grid{display:grid;grid-template-columns:repeat(4,250px);grid-template-rows:repeat(3,124px);gap:2px;justify-content:center;margin-top:36px}
.tile{position:relative}
.tile .tag{position:absolute;left:20px;bottom:12px;background:var(--blue);color:var(--white);font-size:11px;padding:3px 12px}
.lower{height:424px;display:flex;padding:110px 100px 0 100px;gap:70px}
.reviews{width:600px}
.reviews h2,.partners h2{font-size:22px;font-weight:300;color:#555}
.quote{margin-top:24px;border:1px solid var(--line);height:150px;padding:22px 26px;display:flex;gap:18px}
.quote .avatar{width:54px;height:54px;border-radius:50%;background:#cfcfcf;flex:none}
.quote .who{font-size:13px;color:#555}
.quote .who span{font-size:10px;color:var(--muted);margin-left:8px}
.quote p{font-size:10px;color:#888;line-height:14px;margin-top:8px}
.dots{display:flex;gap:6px;justify-content:center;margin-top:12px}
.dots i{width:7px;height:7px;border-radius:50%;background:#ccc}
.dots i.on{background:var(--blue)}
.partners{width:340px;text-align:center}
.logos{display:grid;grid-template-columns:repeat(3,96px);gap:24px 18px;margin-top:34px;justify-content:center}
.logos div{height:56px;background:#ececec}
.footer{position:absolute;top:2214px;left:0;width:1200px;height:44px;background:var(--green);display:flex;justify-content:space-between;align-items:center;padding:0 100px}
.footer .links{font-size:12px;color:var(--white)}
.footer .cards{display:flex;gap:4px}
.footer .cards i{width:26px;height:17px;background:var(--white);border-radius:2px}
.copyright{position:absolute;top:2286px;left:100px;font-size:12px;color:#666}
</style>
</head>
<body>
<div class="page">
  <div class="topbar">
    <div class="links"><span>Login</span>|<span>Signup</span>|<span>Privacy</span>|<span>About Us</span></div>
    <div class="follow">Follow Us <i class="dot"></i><i class="dot"></i><i class="dot"></i><i class="dot"></i><i class="dot"></i></div>
  </div>
  <header class="header">
    <div class="brand"><span class="mark"></span><span class="name">Fernhollow Glow Clinic</span></div>
    <nav class="nav">
      <a class="active">Home</a><a>About Us</a><a>Site Map</a><a>FAQs</a><a>Contact Us</a>
      <span class="search"><svg width="20" height="20" viewBox="0 0 20 20"><circle cx="8" cy="8" r="6" fill="none" stroke="#33a6d7" stroke-width="2.5"/><line x1="12.5" y1="12.5" x2="18" y2="18" stroke="#33a6d7" stroke-width="3"/></svg></span>
    </nav>
  </header>
  <section class="hero" role="img" aria-label="Therapist treating a client's arm with a laser therapy device">
    <div class="tagline"><div class="small">Come and experience the</div><div class="big">Wellness of life in nature</div></div>
    <span class="arrow left"><svg width="10" height="14"><path d="M8 1 2 7l6 6" fill="none" stroke="#fff" stroke-width="2"/></svg></span>
    <span class="arrow right"><svg width="10" height="14"><path d="M2 1l6 6-6 6" fill="none" stroke="#fff" stroke-width="2"/></svg></span>
  </section>
  <div class="rule"></div>
  <section class="services">
    <div class="service"><div class="photo" role="img" aria-label="Cosmetic injection treatment" style="background:radial-gradient(#e7cbb5,#c9a48a)"></div><h3>Cosmetic Injections</h3><p>Lorem Ipsum is simply dummy text of the printing and typesetting industry.</p><span class="btn-more primary">More</span></div>
    <div class="service"><div class="photo" role="img" aria-label="Podiatry foot care" style="background:radial-gradient(#f0d6c3,#d9b296)"></div><h3>Podiatry</h3><p>Lorem Ipsum is simply dummy text of the printing and typesetting industry.</p><span class="btn-more">More</span></div>
    <div class="service"><div class="photo" role="img" aria-label="Remedial back massage" style="background:radial-gradient(#eccab0,#c59576)"></div><h3>Remedial Massage</h3><p>Lorem Ipsum is simply dummy text of the printing and typesetting industry.</p><span class="btn-more">More</span></div>
    <div class="service"><div class="photo" role="img" aria-label="Laser therapy session" style="background:radial-gradient(#e9e2dc,#c7b3a4)"></div><h3>Laser Therapies</h3><p>Lorem Ipsum is simply dummy text of the printing and typesetting industry.</p><span class="btn-more">More</span></div>
    <div class="service"><div class="photo" role="img" aria-label="Skin care treatment" style="background:radial-gradient(#f3e3d6,#d7b9a2)"></div><h3>Skin Care</h3><p>Lorem Ipsum is simply dummy text of the printing and typesetting industry.</p><span class="btn-more">More</span></div>
  </section>
  <section class="newsletter" role="img" aria-label="Relaxing spa backdrop">
    <svg width="34" height="28" viewBox="0 0 34 28"><path d="M1 13 33 1 26 27 16 18 1 13Z M16 18 33 1" fill="none" stroke="#fff" stroke-width="2" stroke-linejoin="round"/></svg>
    <div class="label">Subscribe to our<br>Newsletter</div>
    <div class="field">Enter Your Name</div>
    <div class="field wide">Enter Your Email Address</div>
    <div class="submit">SUBSCRIBE</div>
  </section>
  <section class="gallery">
    <h2>OUR GALLERY</h2><div class="bar"></div>
    <div class="sub">Take a look at our practice and pictures of our day spa</div>
    <div class="grid">
      <div class="tile" role="img" aria-label="Facial treatment" style="background:linear-gradient(135deg,#d8c1b0,#a98b78)"><span class="tag">Read More</span></div>
      <div class="tile" role="img" aria-label="Hot stone massage" style="background:linear-gradient(135deg,#c79a7d,#8a5e45)"></div>
      <div class="tile" role="img" aria-label="Clay face mask" style="background:linear-gradient(135deg,#8d8579,#5c564d)"></div>
      <div class="tile" role="img" aria-label="Pedicure with flowers" style="background:linear-gradient(135deg,#ead9cb,#c9a98f)"></div>
      <div class="tile" role="img" aria-label="Back massage" style="background:linear-gradient(135deg,#dcae8f,#a8735a)"></div>
      <div class="tile" role="img" aria-label="Spa candles and stones" style="background:linear-gradient(135deg,#5a4a3c,#c9b27a)"></div>
      <div class="tile" role="img" aria-label="Relaxing facial" style="background:linear-gradient(135deg,#e7d3c2,#b99781)"></div>
      <div class="tile" role="img" aria-label="Foot spa" style="background:linear-gradient(135deg,#d6b9a2,#9d7860)"></div>
      <div class="tile" role="img" aria-label="Towels and orchids" style="background:linear-gradient(135deg,#f1ece6,#cfc4bb)"></div>
      <div class="tile" role="img" aria-label="Candle treatment" style="background:linear-gradient(135deg,#d9c69a,#8d6f44)"></div>
      <div class="tile" role="img" aria-label="Hand massage" style="background:linear-gradient(135deg,#e5c8b2,#b38a6f)"></div>
      <div class="tile" role="img" aria-label="Spa bowl with petals" style="background:linear-gradient(135deg,#e2d7c4,#a99d7d)"></div>
    </div>
  </section>
  <section class="lower">
    <div class="reviews">
      <h2>WHAT CUSTOMERS SAY ABOUT US</h2>
      <div class="quote">
        <span class="avatar"></span>
        <div>
          <div class="who">Clara Wendt <span>— Happy Client</span></div>
          <p>Friendly staff, calm rooms and results I truly love. Every visit feels like a short escape, and my skin has never looked brighter. I recommend the team to all my friends.</p>
          <div class="dots"><i class="on"></i><i></i><i></i></div>
        </div>
      </div>
    </div>
    <div class="partners">
      <h2>Our Partners</h2>
      <div class="logos"><div></div><div></div><div></div><div></div><div></div><div></div></div>
    </div>
  </section>
  <footer class="footer">
    <div class="links">Sitemap | About | Services | Graduate | Contact Us</div>
    <div class="cards"><i></i><i></i><i></i><i></i></div>
  </footer>
  <div class="copyright">Copyright 2016. All Rights Reserved.</div>
</div>
</body>
</html>
```